Investment company needing business card

We are wanting a business card which looks sharp and easy on the eye. We are thinking of having a business card with the logo embossed on it, to really make it stand out. We will only have a small amount of information of the business card, person's name, position, email address and phone number

Contact Information for Business Card

Danica Pruett
Executive Assistant
+64 21 547 3162
danicap@harwellcapital.co.nz

Requirements
Must have
• Embossed logo
Should not have
• Not to be busy

```html
<!DOCTYPE html>
<html lang="en">
<head>
<meta charset="utf-8">
<title>Harwell Capital – Business Card</title>
<link href="https://fonts.googleapis.com/css2?family=Roboto:wght@400;500;700&display=swap" rel="stylesheet">
<style>
  :root {
    --backdrop: #2e3f47;
    --card: #0b0c0c;
    --accent: #1fc27a;
    --text-light: #d9dcdc;
    --text-muted: #b4b8b8;
    --divider: #8c8f90;
  }
  * { margin: 0; padding: 0; box-sizing: border-box; }
  html, body {
    width: 1200px; height: 1200px; overflow: hidden;
    background: var(--backdrop);
    font-family: "Roboto", Arial, sans-serif;
  }
  .business-card {
    position: absolute;
    left: 75px; top: 300px;
    width: 1050px; height: 600px;
    background: var(--card);
    box-shadow: 0 20px 50px rgba(0,0,0,0.45);
  }
  .brand {
    position: absolute;
    left: 70px; top: 242px;
    display: flex; align-items: center; gap: 14px;
    white-space: nowrap;
  }
  .brand-mark {
    width: 56px; height: 56px;
    background: var(--accent);
    flex: none;
  }
  .brand-name {
    color: var(--accent);
    font-weight: 500;
    font-size: 32px;
    letter-spacing: 1px;
    line-height: 1;
    text-transform: uppercase;
  }
  .divider {
    position: absolute;
    left: 545px; top: 172px;
    width: 5px; height: 210px;
    background: var(--divider);
  }
  .contact-block {
    position: absolute;
    left: 590px; top: 168px;
    white-space: nowrap;
  }
  .person-name {
    color: var(--accent);
    font-weight: 500;
    font-size: 42px;
    line-height: 1.05;
  }
  .person-title {
    display: inline-block;
    color: var(--text-muted);
    font-size: 24px;
    padding-bottom: 4px;
    border-bottom: 2px solid var(--text-muted);
  }
  .contact-list { list-style: none; margin-top: 44px; }
  .contact-item {
    display: flex; align-items: center; gap: 14px;
    color: var(--text-light);
    font-weight: 500;
    font-size: 24px;
    margin-bottom: 12px;
  }
  .contact-icon { width: 24px; height: 24px; flex: none; }
</style>
</head>
<body>
  <div class="business-card">
    <div class="brand">
      <div class="brand-mark"></div>
      <div class="brand-name">Harwell Capital</div>
    </div>

    <div class="divider"></div>

    <div class="contact-block">
      <div class="person-name">Danica Pruett</div>
      <div class="person-title">Executive Assistant</div>
      <ul class="contact-list">
        <li class="contact-item">
          <svg class="contact-icon" viewBox="0 0 24 24" fill="none" stroke="var(--accent)" stroke-width="1.5">
            <rect x="2" y="2" width="20" height="20" rx="3"/>
            <path d="M8 6c-1.5 1-2 3 0 7s4.5 5.5 6.5 5l1.5-2-2.5-2-1.5 1c-1-.5-2.5-2.5-3-4l1-1.3L8.5 6z"/>
          </svg>
          <span>+64 21 547 3162</span>
        </li>
        <li class="contact-item">
          <svg class="contact-icon" viewBox="0 0 24 24" fill="none" stroke="var(--accent)" stroke-width="1.5">
            <rect x="1.5" y="5" width="21" height="14"/>
            <path d="M1.5 5l10.5 8 10.5-8M1.5 19l8-7M22.5 19l-8-7"/>
          </svg>
          <span>danicap@harwellcapital.co.nz</span>
        </li>
      </ul>
    </div>
  </div>
</body>
</html>
```